Business Cards PLRB

Business cards redesign, front and back. Dimensions 45mm x 85mm. Stylish, creative and professional designed business cards. You can use actual logo (attached) or design a new one to suit your design (I am happy to pay extra $50 for new logo IF APPROVED). Try to incorporate some blue. Check website if needed www.plumlanternridesbackwards.com.au. All files need to be delivered as .jpg .pdf. eps .ai If logo is redesigned, separate file of logo should also be delivered as .jpg .pdf .eps .ai. Winner will have priority to design stationery on a near future. Winner needs to be willing to do some changes if necessary. Please find attached actual business card.

```html
<!DOCTYPE html>
<html lang="en">
<head>
<meta charset="utf-8">
<title>PLRB Business Cards</title>
<link rel="stylesheet" href="https://fonts.googleapis.com/css2?family=Open+Sans:wght@400;600;700&display=swap">
<style>
  :root {
    --stage: #d9dde2;
    --navy-top: #0a0c5a;
    --navy-bottom: #2a3aa8;
    --panel-light: #1f6f9e;
    --panel-dark: #0b3558;
    --pattern-dark: #14161a;
    --pattern-mid: #2b2f36;
    --accent-cyan: #1aa3cf;
    --moon: #f2cc3a;
    --ink-light: #ffffff;
    --ink-soft: #dce8f2;
    --ink-dark: #3a3a3a;
    --card-white: #fdfdfd;
  }
  html, body {
    margin: 0;
    padding: 0;
    width: 1200px;
    height: 1137px;
    overflow: hidden;
    background: var(--stage);
    font-family: "Open Sans", Verdana, sans-serif;
  }
  .canvas {
    position: relative;
    width: 1200px;
    height: 1137px;
  }
  .card {
    position: absolute;
    left: 150px;
    width: 900px;
    height: 476px;
    overflow: hidden;
    box-shadow: 0 8px 24px rgba(0,0,0,0.25);
  }
  .card--front { top: 70px; background: var(--panel-dark); }
  .card--back { top: 590px; background: var(--card-white); }

  /* front: brand band */
  .brand-band {
    position: absolute;
    left: 0; top: 0;
    width: 900px; height: 118px;
    background: linear-gradient(180deg, var(--navy-top), var(--navy-bottom));
  }
  .brand-name {
    position: absolute;
    font-weight: 600;
    letter-spacing: 0.5px;
    white-space: nowrap;
  }
  .brand-band .brand-name {
    left: 14px; top: 58px;
    font-size: 33px;
    color: var(--ink-light);
  }
  .brand-mark {
    position: absolute;
    border-radius: 50%;
    background: var(--moon);
  }
  .brand-band .brand-mark { left: 790px; top: 40px; width: 62px; height: 62px; }

  /* front: contact panel */
  .contact-panel {
    position: absolute;
    left: 0; top: 118px;
    width: 512px; height: 358px;
    background: radial-gradient(ellipse at 60% 25%, var(--panel-light), var(--panel-dark) 85%);
    color: var(--ink-soft);
    text-align: center;
  }
  .contact-heading {
    margin: 0;
    position: absolute;
    left: 0; right: 0; top: 14px;
    font-size: 27px;
    font-weight: 700;
    color: var(--ink-light);
  }
  .address {
    position: absolute;
    left: 0; right: 0; top: 66px;
    font-size: 20px;
    font-weight: 600;
    line-height: 24px;
  }
  .address strong { color: var(--ink-light); font-size: 22px; }
  .contact-list {
    position: absolute;
    left: 10px; top: 128px;
    margin: 0; padding: 0;
    list-style: none;
    text-align: left;
    font-size: 17px;
    line-height: 27px;
    color: var(--ink-light);
  }
  .contact-list li { display: flex; align-items: center; gap: 8px; }
  .contact-list li.web { font-size: 15px; }
  .contact-list svg { width: 18px; height: 18px; flex: none; }
  .abn-label {
    position: absolute;
    left: 0; right: 0; top: 266px;
    font-size: 21px;
    font-weight: 700;
    color: var(--ink-light);
  }
  .abn-number {
    position: absolute;
    left: 0; right: 0; top: 298px;
    font-size: 23px;
    color: var(--ink-light);
  }

  /* front: pattern panel */
  .pattern-panel {
    position: absolute;
    left: 512px; top: 118px;
    width: 388px; height: 358px;
    background:
      radial-gradient(circle at 30% 35%, rgba(26,163,207,0.35), transparent 45%),
      radial-gradient(circle at 80% 75%, rgba(26,163,207,0.3), transparent 40%),
      linear-gradient(135deg, var(--pattern-mid), var(--pattern-dark));
  }
  .person {
    position: absolute;
    right: 14px; top: 160px;
    text-align: right;
    color: var(--ink-light);
  }
  .person-name {
    margin: 0;
    font-size: 27px;
    font-weight: 600;
    letter-spacing: 3px;
  }
  .person-title {
    margin: 4px 0 0;
    font-size: 16px;
    font-weight: 700;
    letter-spacing: 2px;
  }

  /* back */
  .card--back .brand-name {
    left: 40px; top: 230px;
    font-size: 36px;
    color: var(--ink-dark);
  }
  .card--back .brand-mark { left: 770px; top: 170px; width: 78px; height: 78px; }
</style>
</head>
<body>
<main class="canvas">

  <section class="card card--front" aria-label="Business card front">
    <header class="brand-band">
      <span class="brand-name">...and the plum lantern rides backwards</span>
      <span class="brand-mark" aria-hidden="true"></span>
    </header>

    <div class="contact-panel">
      <h2 class="contact-heading">Address</h2>
      <p class="address" style="margin:0">Harbour Rise, NSW, 2999<br><strong>Australia</strong></p>
      <ul class="contact-list">
        <li>
          <svg viewBox="0 0 20 20" aria-hidden="true"><circle cx="10" cy="10" r="9" fill="#fff"/><path d="M7 5c1 0 2 2 2 3s-1 1-1 2 2 3 3 3 1-1 2-1 3 1 3 2-1 2-2 2C9 16 4 11 4 7c0-1 2-2 3-2z" fill="#0b3558" transform="scale(.8) translate(2.5 2.5)"/></svg>
          0400 555 018
        </li>
        <li>
          <svg viewBox="0 0 20 20" aria-hidden="true"><rect x="2" y="5" width="16" height="11" fill="#fff"/><path d="M2 5l8 6 8-6" stroke="#0b3558" stroke-width="1.5" fill="none"/></svg>
          info@plumlanternridesbackwards.com.au
        </li>
        <li class="web">
          <svg viewBox="0 0 20 20" aria-hidden="true"><circle cx="10" cy="10" r="8" fill="none" stroke="#fff" stroke-width="2"/><path d="M2 10h16M10 2c-3 3-3 13 0 16M10 2c3 3 3 13 0 16" stroke="#fff" stroke-width="1.5" fill="none"/></svg>
          www.plumlanternridesbackwards.com.au
        </li>
      </ul>
      <div class="abn-label">Australian Business Number</div>
      <div class="abn-number">12 345 678 901</div>
    </div>

    <div class="pattern-panel" role="img" aria-label="Decorative pattern of dark cubes with blue accents">
      <div class="person">
        <p class="person-name">Maren Holloway</p>
        <p class="person-title">Designer de Interiores</p>
      </div>
    </div>
  </section>

  <section class="card card--back" aria-label="Business card back">
    <span class="brand-name">...and the plum lantern rides backwards</span>
    <span class="brand-mark" aria-hidden="true"></span>
  </section>

</main>
</body>
</html>
```